High-end executive coaching group needs a 2 page digital flyer

We need a 2 page digital flyer for a high end leadership coaching offering for global leaders in healthcare. The flyer will advertise a new service (an elite senior leadership coaching group) for senior leaders in the healthcare industry from around the world.
The flyer should be upmarket, professional and minimalist in style to meet the expectations of my professional market (very senior doctors and executives).
The design should be based on my existing logo and brand, see my landing page: www.marlowadvisory.com
The key elements needed are
1) An editable PDF which we can update as we revise the specific details of the offering. The text and draft design for this is attached.
2) The banner image should be high quality but abstract. It can be based on the landing page of my website (the two ripple effects) but does not need to strictly adhere to this.
3) The logo placement of the Marlow Advisory delta sign should be discreet so that it does not dominate
4) The small logos of our professional accrediting organisations should be discreetly placed at the end and should not dominate. They might work best as mono icons in a footer (e.g. blue on a white background, or white on blue.
5) Please find enclosed a previous flyer as an example of a similar style we have used for more junior professionals. The design worked quite well, although we now need a more upmarket version for our senior executives.
Updates

Please note this design specifically needs to use existing branding and images from my website: marlowadvisory.com. We are definitely not looking for stock "leadership team" images for this high-end brochure.

Target Market(s)

Senior global leaders in the healthcare industry

Industry/Entity Type

Leading business schools & Healthcare industry.

Font styles to use
Other font styles liked:
• Operetta (selective use for heading) and Sofia Pro (body text)

Colors
0054AA
0677BA
7BADD7
CADEEF
E8F1F8

Requirements
Must have
• Clean minimalist and high professionally look that directly speaks to the interests and perspectives of senior leader leaders in healthcare. It also needs very clear call to action sections
Nice to have
• Effective presentation of the two bios and photographs. These need to look impressive, but should not dominate.
Should not have
• Loud and bold colours, large use of logos.

```html
<!DOCTYPE html>
<html lang="en">
<head>
<meta charset="utf-8">
<title>Marlow Advisory – Analytic Coaching Group flyer</title>
<link href="https://fonts.googleapis.com/css2?family=Libre+Caslon+Text:wght@400&family=Lexend:wght@300;400;700;800&display=swap" rel="stylesheet">
<style>
:root{
  --navy:#2c3168;
  --brand:#1f4fa0;
  --band:#d5e7f6;
  --bubble:#5aaae0;
  --tick:#4a9bd7;
  --ink:#4d4d55;
  --white:#ffffff;
  --backdrop:#a9a8a9;
}
*{margin:0;padding:0;box-sizing:border-box}
html,body{width:1200px;height:1117px;overflow:hidden}
body{background:var(--backdrop);font-family:"Lexend",sans-serif;color:var(--ink);position:relative}
.page{position:absolute;top:176px;width:896px;height:1268px;background:var(--white);transform:scale(0.6036);transform-origin:0 0;overflow:hidden;box-shadow:6px 8px 14px rgba(0,0,0,.25)}
.page--front{left:51px}
.page--back{left:608px}
.abs{position:absolute}
.serif{font-family:"Libre Caslon Text",serif;font-weight:400}
.brand-name{font-family:"Libre Caslon Text",serif;color:var(--brand);font-size:40px;line-height:40px;display:flex;align-items:center;gap:16px}
.brand-name .mark{width:22px;height:22px;background:var(--brand)}
.hero-title{left:77px;top:190px;color:var(--white);font-size:43px;line-height:48px}
.hero-sub{left:77px;top:294px;width:440px;color:var(--white);font-weight:800;font-size:15px;line-height:19.5px}
.quote{background:var(--bubble);border-radius:24px;color:var(--white);text-align:center;font-weight:300;font-size:16px;line-height:19.5px;padding:14px 18px}
.quote .mark{font-family:"Lexend",sans-serif;font-weight:800;font-style:italic;font-size:38px;line-height:30px;display:block}
.quote .by{font-weight:700;margin-top:8px;display:block}
.section-title{color:var(--navy);font-size:21px}
.body-text{font-weight:300;font-size:16px;line-height:19.5px}
.band{background:var(--band);left:0;right:0}
.benefit{display:flex;gap:20px;width:360px}
.tick{flex:none;width:15px;height:15px;border-radius:50%;background:var(--tick);position:relative;margin-top:2px}
.tick::after{content:"";position:absolute;left:4px;top:3px;width:6px;height:4px;border-left:2px solid #fff;border-bottom:2px solid #fff;transform:rotate(-45deg)}
.benefit b{color:var(--navy);font-weight:700;display:block;font-size:16px;line-height:19.5px}
.details{left:77px;top:886px;width:743px;font-size:16px}
.details .row{display:flex;min-height:36px;padding:8px 0 6px 37px}
.details .row:nth-child(even){background:var(--band)}
.details .label{width:165px;font-weight:700;color:var(--navy)}
.details .value{font-weight:300;color:#333;line-height:18px}
.cta{left:77px;top:1094px;width:743px;height:38px;border:2px solid var(--navy);border-radius:12px;color:var(--navy);font-weight:800;font-size:20px;display:flex;align-items:center;justify-content:center}
.book{left:77px;top:1147px;color:var(--navy);font-size:29px}
.badges{left:515px;top:1150px;display:flex;gap:18px;align-items:center}
.badge{background:#c9cde0;height:30px}
.footer{left:0;top:1203px;width:896px;height:65px}
.contact{top:1220px;color:var(--white);font-weight:700;font-size:16px;display:flex;align-items:center;gap:10px}
.contact--web{color:var(--navy)}
.contact .dot{width:14px;height:14px;border-radius:50%;background:var(--tick)}
.contact--web .dot{background:var(--navy)}
.photo{border-radius:18px;overflow:hidden}
.photo-frame{background:#a8cdec;border-radius:18px}
.bio{font-weight:300;font-size:15.5px;line-height:19.3px;color:#3e3e46}
.lead-q{color:var(--navy);font-weight:700;font-size:15.5px;line-height:22px}
.question{display:flex;gap:22px;width:440px}
</style>
</head>
<body>

<!-- FRONT PAGE -->
<section class="page page--front">
  <svg class="abs" style="left:0;top:0" width="896" height="380" viewBox="0 0 896 380">
    <defs>
      <linearGradient id="sky" x1="0" y1="0" x2="0" y2="1">
        <stop offset="0" stop-color="#9ec7e4"/>
        <stop offset=".5" stop-color="#c9dbe6"/>
        <stop offset="1" stop-color="#2a2d35"/>
      </linearGradient>
    </defs>
    <path d="M350 0 L896 0 L896 378 L0 378 L0 171 L435 171 Z" fill="#2c3168"/>
    <path d="M372 0 L896 0 L896 347 L620 347 Q552 347 522 292 Z" fill="#ffffff"/>
    <path d="M384 0 L896 0 L896 335 L628 335 Q566 335 538 286 Z" fill="url(#sky)" role="img" aria-label="Photo area: silhouetted group on a mountain top at sunrise"/>
  </svg>

  <div class="abs brand-name" style="left:77px;top:70px"><span class="mark"></span>Marlow<br>Advisory</div>

  <h1 class="abs serif hero-title">Elevate and Ignite<br>Your Leadership</h1>
  <p class="abs hero-sub">Transformative conversations for senior healthcare leaders. Unlock purpose, engage authentically and amplify your leadership impact.</p>

  <div class="abs band" style="top:600px;height:276px"></div>

  <h2 class="abs serif section-title" style="left:77px;top:398px">Analytic Coaching Group for Senior Leaders</h2>
  <p class="abs body-text" style="left:77px;top:432px;width:450px">As a senior leader in healthcare, you’re constantly navigating challenges. But where do you turn for authentic connections, reflection and personal growth?</p>
  <p class="abs body-text" style="left:77px;top:509px;width:440px">Rethink your leadership assumptions and approach challenges with fresh creativity. Secure your spot in our exclusive Analytic Coaching Group and ignite your leadership potential.</p>

  <blockquote class="abs quote" style="left:541px;top:360px;width:299px;height:262px">
    <span class="mark">“</span>
    You bare your heart and share things you wouldn’t under normal circumstances. You get to know each other very quickly. There’s that sort of intense, shared experience that comes from speaking to each other’s lives.
    <span class="by">-Sarah, Medical Director</span>
    <span class="mark">”</span>
  </blockquote>

  <h2 class="abs serif section-title" style="left:77px;top:610px">Benefits to you</h2>
  <div class="abs benefit" style="left:77px;top:650px"><span class="tick"></span><p class="body-text"><b>Transformative conversations:</b>Engage in discussions that spark innovative leadership</p></div>
  <div class="abs benefit" style="left:460px;top:650px"><span class="tick"></span><p class="body-text"><b>Instant 360° insights:</b>Gain real-time feedback from trusted peers to enrich your leadership</p></div>
  <div class="abs benefit" style="left:77px;top:720px"><span class="tick"></span><p class="body-text"><b>Peer insights:</b>Harness fresh insights from peers, enhancing your decision-making and effectiveness</p></div>
  <div class="abs benefit" style="left:460px;top:720px"><span class="tick"></span><p class="body-text"><b>Lead authentically:</b>Develop effective strategies using the latest insights from group and leadership psychology</p></div>
  <div class="abs benefit" style="left:77px;top:808px;width:500px"><span class="tick"></span><p class="body-text"><b>Reimagined leadership:</b>Channel your creativity and redefine your leadership, personally and professionally</p></div>

  <div class="abs details">
    <div class="row"><span class="label">Dates:</span><span class="value">7 February 2024 – 11 December 2024</span></div>
    <div class="row"><span class="label">Time:</span><span class="value">7:30am - 8:45am (UK time).</span></div>
    <div class="row"><span class="label">Commitment:</span><span class="value">Wednesdays, every 2 weeks</span></div>
    <div class="row"><span class="label">Location:</span><span class="value">Connect from anywhere by video link</span></div>
    <div class="row"><span class="label">Cost:</span><span class="value" style="width:520px">Cost: £3350 [UK] €3900 [Europe] A$6530 [Australia] Payment options available</span></div>
  </div>

  <div class="abs cta">Secure your spot now and ignite your leadership potential..</div>

  <p class="abs serif book">Book your free discovery call</p>
  <div class="abs badges">
    <span class="badge" style="width:32px;height:32px;border-radius:50%"></span>
    <span class="badge" style="width:60px"></span>
    <span class="badge" style="width:54px"></span>
    <span class="badge" style="width:96px"></span>
  </div>

  <svg class="abs footer" width="896" height="65" viewBox="0 0 896 65">
    <rect width="896" height="65" fill="#2c3168"/>
    <path d="M896 0 L580 0 Q605 0 615 25 Q628 50 660 50 L896 50 Z" fill="#d5e7f6"/>
  </svg>
  <p class="abs contact" style="left:77px"><span class="dot"></span>daniel@marlowadvisory.com</p>
  <p class="abs contact" style="left:369px"><span class="dot"></span>helenashby@mailbox.net</p>
  <p class="abs contact contact--web" style="left:628px"><span class="dot"></span>marlowadvisory.com</p>
</section>

<!-- BACK PAGE -->
<section class="page page--back">
  <div class="abs" style="left:0;top:50px;width:498px;height:118px;background:#a8cdec;border-radius:0 14px 14px 0"></div>
  <div class="abs" style="left:0;top:42px;width:492px;height:118px;background:var(--navy);border-radius:0 14px 14px 0"></div>
  <h2 class="abs serif" style="left:73px;top:50px;color:#fff;font-size:27px;line-height:32px">Expertly guided by insight,<br>academic rigour and practical<br>leadership strategies</h2>

  <div class="abs brand-name" style="left:540px;top:70px"><span class="mark"></span>Marlow<br>Advisory</div>

  <div class="abs band" style="top:185px;left:340px;height:275px"></div>
  <div class="abs photo-frame" style="left:88px;top:198px;width:265px;height:278px"></div>
  <div class="abs photo" style="left:73px;top:185px;width:265px;height:275px;background:linear-gradient(160deg,#7ea86a,#3e5e8e)" role="img" aria-label="Portrait photo of the lead coach"></div>
  <p class="abs bio" style="left:385px;top:207px;width:450px">Professor Daniel Marlow has 30 years’ experience developing leaders. An award-winning business school professor, group analyst and psychoanalytic psychotherapist, he has taught senior leadership programmes at the University of Ardley, Kingsmere College and the University of Southbay. His extensive leadership experience as a national health service clinical director and consultant psychotherapist inform his work as an accredited executive coach. With a PhD from Westbrook College, he is an expert in melding psychological insights with strategic organisational change.</p>

  <div class="abs band" style="top:495px;right:auto;width:560px;height:275px"></div>
  <div class="abs photo-frame" style="left:568px;top:506px;width:265px;height:278px"></div>
  <div class="abs photo" style="left:553px;top:493px;width:265px;height:273px;background:linear-gradient(180deg,#1a1414,#3a2a26 60%,#d9a89a)" role="img" aria-label="Portrait photo of the co-facilitator"></div>
  <p class="abs bio" style="left:73px;top:518px;width:430px">Dr Helen Ashby is a renowned psychoanalyst, group analyst, consultant psychiatrist and organisational consultant in the health sector. She has 20 years of leadership within the national health service, and she was also the National Director of Therapies for the Larkfield Group, directing therapy services across 100 UK hospitals. She holds prominent positions as Chair of the Patient Safety Group, Chair of the Working Group on the Effect of Suicide and Homicide on Psychiatrists, and Vice Chair of the Psychotherapy Faculty at the Royal Guild of Psychiatrists.</p>

  <p class="abs lead-q" style="left:73px;top:841px;width:440px">Engage with global leaders, gain diverse insights and forge lasting bonds. Explore questions such as:</p>
  <div class="abs question" style="left:73px;top:898px"><span class="tick"></span><p class="body-text">What kind of leader do I aspire to be in the next chapter of my life and career?</p></div>
  <div class="abs question" style="left:73px;top:956px"><span class="tick"></span><p class="body-text">What unique qualities and actions do I offer that no one else can?</p></div>
  <div class="abs question" style="left:73px;top:1014px"><span class="tick"></span><p class="body-text">How can I galvanise my personal strengths to inspire and motivate others?</p></div>

  <blockquote class="abs quote" style="left:541px;top:803px;width:299px;height:270px;padding-top:16px">
    <span class="mark">“</span>
    Through this exceptional coaching, our leadership team elevated its performance to lead the hospital with greater clarity, cohesion and thoughtfulness. Not only do we provide a superior work environment for staff, but better care for our patients.
    <span class="by">John, CEO</span>
    <span class="mark">”</span>
  </blockquote>

  <p class="abs" style="left:0;width:896px;top:1090px;text-align:center;color:var(--navy);font-weight:700;font-size:15.5px">Limited spots available</p>
  <p class="abs body-text" style="left:0;width:896px;top:1113px;text-align:center">Don’t miss this unique opportunity to transform your leadership journey.</p>

  <p class="abs serif book">Book your free discovery call</p>
  <div class="abs badges">
    <span class="badge" style="width:32px;height:32px;border-radius:50%"></span>
    <span class="badge" style="width:60px"></span>
    <span class="badge" style="width:54px"></span>
    <span class="badge" style="width:96px"></span>
  </div>

  <svg class="abs footer" width="896" height="65" viewBox="0 0 896 65">
    <rect width="896" height="65" fill="#2c3168"/>
    <path d="M896 0 L580 0 Q605 0 615 25 Q628 50 660 50 L896 50 Z" fill="#d5e7f6"/>
  </svg>
  <p class="abs contact" style="left:77px"><span class="dot"></span>daniel@marlowadvisory.com</p>
  <p class="abs contact" style="left:369px"><span class="dot"></span>helenashby@mailbox.net</p>
  <p class="abs contact contact--web" style="left:628px"><span class="dot"></span>marlowadvisory.com</p>
</section>

</body>
</html>
```